When the boots match march on! book cover design

Book cover for a business, non-fiction book.
About stepping up, being who you truly are, and willing not to fit in.

TITLE: When The Boots Match, March On!
SUBTITLE: Quit copying the chief others expect of you and begin shaping the chief nobody else could ever shape...
AUTHOR: Tobias Hartwell-Brenner
Updates

we never uploaded the brief

Target Market(s)

Business people, curious leaders, insiders who have a secret itch to be an outsider
AGE: 35-50 years old

Font styles to use
Sans Serif
Other font styles liked:
• designer's choice!

Requirements
Must have
• Very visual
Imagery must reflect the topic of the book

```html
<!DOCTYPE html>
<html lang="en">
<head>
<meta charset="utf-8">
<title>When The Boots Match, March On! — Book Cover</title>
<link rel="stylesheet" href="https://fonts.googleapis.com/css2?family=Playfair+Display:wght@400;500&display=swap">
<style>
  :root {
    --paper: #ffffff;
    --title-red: #d20a2e;
    --ink: #141414;
    --sky-top: #6f6a86;
    --sky-glow: #f2b36a;
    --sun: #fbe7a2;
    --cape-red: #b3121f;
    --suit: #2f3246;
    --city: #c98a4a;
  }
  * { margin: 0; padding: 0; box-sizing: border-box; }
  html, body {
    width: 840px;
    height: 1200px;
    overflow: hidden;
    background: var(--paper);
  }
  .cover {
    position: relative;
    width: 840px;
    height: 1200px;
    background: var(--paper);
    font-family: "Playfair Display", Georgia, serif;
  }
  .cover-photo {
    position: absolute;
    left: 0;
    top: 0;
    width: 840px;
    height: 600px;
    background:
      radial-gradient(ellipse 55% 50% at 92% 45%, var(--sun) 0%, rgba(251,231,162,0) 70%),
      linear-gradient(90deg, var(--cape-red) 0%, var(--cape-red) 22%, rgba(179,18,31,0) 34%),
      linear-gradient(90deg, rgba(47,50,70,0) 30%, var(--suit) 38%, var(--suit) 66%, rgba(47,50,70,0) 72%),
      linear-gradient(180deg, var(--sky-top) 0%, var(--sky-glow) 40%, var(--city) 100%);
  }
  .title {
    position: absolute;
    left: 48px;
    top: 652px;
    color: var(--title-red);
    font-weight: 400;
    line-height: 1;
  }
  .title-line-one {
    display: block;
    font-size: 76px;
    letter-spacing: -0.5px;
  }
  .title-line-two {
    display: block;
    margin-top: 8px;
    font-size: 104px;
    letter-spacing: -3px;
    text-transform: uppercase;
  }
  .subtitle {
    position: absolute;
    left: 48px;
    top: 912px;
    width: 760px;
    color: var(--ink);
    font-size: 23px;
    line-height: 30px;
    font-weight: 400;
  }
  .author {
    position: absolute;
    left: 48px;
    top: 1133px;
    color: var(--ink);
    font-size: 30px;
    font-weight: 400;
    letter-spacing: -0.5px;
    text-transform: uppercase;
  }
</style>
</head>
<body>
  <main class="cover">
    <div class="cover-photo" role="img" aria-label="Businessman in a dark suit with arms crossed and a flowing red cape, standing above a city skyline at golden sunset"></div>
    <h1 class="title">
      <span class="title-line-one">When The Boots Match,</span>
      <span class="title-line-two">March On!</span>
    </h1>
    <p class="subtitle">Quit copying the chief others expect of you and begin shaping<br>the chief nobody else could ever shape...</p>
    <p class="author">Tobias Hartwell-Brenner</p>
  </main>
</body>
</html>
```